Washroom Services - Flyer Design - to compete with international players

I need a flyer to compete with large international suppliers like Bramwell Sanitary who dominate the washroom services market here in New Zealand. Washroom services include supply and replenishment of air fresheners, soaps, sanitisers, hand towels, toilet paper and sanitary disposal units.
Looking at A4 brochure folded to DLE size (ie in 3) recommendations please if another orientation/size would be better.
Target Market(s)
Businesses with multiple washrooms in one site such as office blocks/towers, municiple buildings, restaurants, gyms.
Requirements
Must have
- Clearbrook Supply Logo, images of the dispensers - nb any other logo currently on a dispenser needs the Clearbrook Supply logo photo shopped onto it.
Nice to have
- Icons to represent different product offerings
Should not have
- Any images of people

```html
<!DOCTYPE html>
<html lang="en">
<head>
<meta charset="utf-8">
<title>Clearbrook Supply – Washroom Services Flyer</title>
<link rel="stylesheet" href="https://fonts.googleapis.com/css2?family=Jost:wght@400&display=swap">
<style>
  :root {
    --backdrop: #a6a8ab;
    --navy: #2d4b7d;
    --sky: #4a80c4;
    --ink: #1e1e1e;
    --paper: #ffffff;
    --rule: #c9c9c9;
  }
  * { margin: 0; padding: 0; box-sizing: border-box; }
  html, body { width: 1200px; height: 938px; overflow: hidden; }
  body {
    background: var(--backdrop);
    font-family: "Jost", "Futura", sans-serif;
    position: relative;
  }
  .panel { position: absolute; top: 41px; height: 867px; width: 375px; }
  .panel-left { left: 36px; background: var(--navy); color: var(--paper); }
  .panel-middle {
    left: 411px;
    background: linear-gradient(90deg, #fff 0%, #fff 80%, #eeeeee 100%);
  }
  .panel-right { left: 786px; width: 373px; background: var(--paper); }

  .block { position: absolute; }
  .block h2 {
    font-weight: 400; font-size: 18.5px; line-height: 1.1;
  }
  .block p { font-size: 13.6px; line-height: 17px; }
  .panel-left .block { left: 31px; width: 320px; }
  .panel-left h2 { color: var(--paper); }
  .panel-left p { color: var(--paper); }
  .left-rule {
    position: absolute; left: 31px; top: 156px; width: 311px;
    border-top: 1px solid rgba(255,255,255,0.8);
  }
  .washroom-photo {
    position: absolute; left: 0; top: 384px; width: 375px; height: 300px;
    background: linear-gradient(135deg, #3c3a36 0%, #7d6a52 40%, #a98a68 60%, #4a4640 100%);
  }

  .product h2 { color: var(--sky); font-size: 19.5px; }
  .product p { color: var(--ink); }
  .panel-middle .product { left: 28px; width: 210px; }
  .panel-right .product { left: 22px; width: 205px; }
  .divider { position: absolute; border-top: 1px solid var(--rule); }
  .panel-middle .divider { left: 28px; width: 302px; }
  .panel-right .divider { left: 16px; width: 352px; }

  .unit-shot {
    position: absolute; border-radius: 6px;
    background: linear-gradient(160deg, #fafafa 0%, #e3e4e6 60%, #c9cbce 100%);
  }

  .options {
    position: absolute; left: 0; top: 684px; width: 373px; height: 183px;
    background: var(--navy); color: var(--paper);
  }
  .options h2 { position: absolute; left: 17px; top: 17px; font-weight: 400; font-size: 19.5px; }
  .options p { position: absolute; left: 21px; top: 55px; width: 340px; font-size: 13.6px; line-height: 17px; }
</style>
</head>
<body>

<section class="panel panel-left">
  <div class="block" style="top:30px">
    <h2>Professional Washroom Service</h2>
    <p>Clearbrook Supply is a New Zealand company with years of experience in the washroom services industry. We have a smart range of washroom dispensers and consumables that will complement your environment at an affordable price.</p>
  </div>
  <div class="left-rule"></div>
  <div class="block" style="top:175px">
    <h2>Customised Service</h2>
    <p>We work with you to ensure that you have the most appropriate washroom solution and service schedule in place. This means that you will have the most relevant level of products and visits customised to your organisation. We can work to a flexible arrangement if your business goes through peaks and troughs with visitors to your bathroom so that you don’t pay for products and services you don’t require.</p>
  </div>
  <div class="washroom-photo" role="img" aria-label="Washroom interior with stone vessel basins and mirrors"></div>
  <div class="block" style="top:711px">
    <h2>Service Guarantee</h2>
    <p>Our team are professionals in the washroom services industry and we guarantee the quality of our work with our service guarantee. We are reliable and ensure that all installations, service calls and maintenance are delivered on time, every time.</p>
  </div>
</section>

<section class="panel panel-middle">
  <div class="block product" style="top:30px">
    <h2>Sanitary Disposal Units</h2>
    <p>The Slim Pod is a new and innovative slim line sanitary disposal system. It’s available in automatic or manual units. The Slim Pod takes up minimal space in each cubicle and is wall mounted for easy cleaning underneath.</p>
  </div>
  <div class="unit-shot" style="left:247px;top:26px;width:96px;height:168px" role="img" aria-label="Sanitary disposal units"></div>
  <div class="divider" style="top:202px"></div>

  <div class="block product" style="top:213px">
    <h2>Air Fresheners</h2>
    <p>Our range of air fresheners include both traditional automatic spray units as well as passive aerosol free units. The range of fragrance and odour neutralisers are extensive and will be matched to best suit your environment.</p>
  </div>
  <div class="unit-shot" style="left:243px;top:230px;width:113px;height:112px" role="img" aria-label="Air freshener dispensers"></div>
  <div class="divider" style="top:382px"></div>

  <div class="block product" style="top:394px">
    <h2>Soap Dispensers</h2>
    <p>Soap dispensers are available in standard flowing soap and foaming hand soap varieties. We will make recommendations on the most appropriate soap for your washroom users.</p>
  </div>
  <div class="unit-shot" style="left:256px;top:401px;width:83px;height:120px;border-radius:16px" role="img" aria-label="Soap dispenser"></div>
  <div class="divider" style="top:535px"></div>

  <div class="block product" style="top:546px">
    <h2>Hand Sanitisers</h2>
    <p>Our hand sanitiser units can be used in washrooms, hallways or office situations. You can opt for alcohol free or alcohol based sanitiser solutions.</p>
  </div>
  <div class="unit-shot" style="left:260px;top:546px;width:71px;height:113px;border-radius:14px" role="img" aria-label="Hand sanitiser dispenser"></div>
  <div class="divider" style="top:669px"></div>

  <div class="block product" style="top:686px;width:215px">
    <h2>WC Seat Sanitising Solutions</h2>
    <p>For peace of mind for your bathroom visitors we can provide WC sanitisers. These are available in either a solution form that is administered via toilet tissue or a dispenser loaded with wet wipes.</p>
  </div>
  <div class="unit-shot" style="left:260px;top:688px;width:75px;height:117px;border-radius:14px" role="img" aria-label="WC seat sanitiser dispenser"></div>
</section>

<section class="panel panel-right">
  <div class="block product" style="top:26px">
    <h2>WC/Urinal Sanitisers</h2>
    <p>By fitting a system that pumps a sanitising solution directly into toilets and urinals you will reduce odours and prevent pipe blockages.</p>
  </div>
  <div class="unit-shot" style="left:279px;top:11px;width:58px;height:119px;border-radius:10px" role="img" aria-label="WC and urinal sanitiser unit"></div>
  <div class="divider" style="top:137px"></div>

  <div class="block product" style="top:153px">
    <h2>Toilet Tissue</h2>
    <p>We will work with you to identify the most appropriate toilet paper solution depending on the traffic through your site. This could be jumbo rolls, mini jumbos or individual toilet rolls. Don’t worry about the terminology – it’s our job to come up with the right solution.</p>
  </div>
  <div class="unit-shot" style="left:231px;top:167px;width:123px;height:163px" role="img" aria-label="Jumbo toilet rolls and twin roll dispenser"></div>
  <div class="divider" style="top:361px"></div>

  <div class="block product" style="top:371px">
    <h2>Hand Towels</h2>
    <p>Paper hand towels are available in a range of different types depending on your requirements. As a complementary offering or alternative option we can provide you with a high speed hand dryer.</p>
  </div>
  <div class="unit-shot" style="left:231px;top:388px;width:110px;height:104px" role="img" aria-label="Paper hand towel dispenser"></div>
  <div class="divider" style="top:526px"></div>

  <div class="block product" style="top:540px">
    <h2>Baby Change Station</h2>
    <p>If you anticipate having babies in your bathroom, then our baby change station is an economical and safe option that you can purchase outright.</p>
  </div>
  <div class="unit-shot" style="left:210px;top:542px;width:142px;height:84px" role="img" aria-label="Fold-down baby change station"></div>

  <div class="options">
    <h2>Other Options</h2>
    <p>Our range of washroom dispensers, fixtures and consumables go far beyond the ones we have outlined here. At all times we will ensure that we get a full understanding of your bathroom visitors so that we can make the most appropriate recommendations. If your circumstances change, we will change out products and services as you require.</p>
  </div>
</section>

</body>
</html>
```